Book: The Seasoned Steward - Good Living IS NOT a Bystander Game

This book is about taking action, and being involved in making health decisions. The title of the book tells two things. First, this book helps people control their health outcomes better. Secondly, that you cannot get great results by just letting doctors make decisions for you (as a spectator). A cover could either show (1) An empowered patient who is "examining" or "influencing" their health outcomes, OR (2) A passive patient watching what is happening. It can be abstract.

All this is for the back of the book: You have been led to believe that two things count when it comes to outcomes: the skills of our practitioners and the effectiveness of the treatments they provide. You don’t even factor yourself into the equation! But you certainly should. You would not want a mediocre doctor, so why be a so-so patient or a passive healthcare consumer? The more evolved and involved you are as a patient and consumer, the closer your healthcare will come to match your needs and your goals. The archetypical relationship we have with healthcare providers needs to be kicked to the curb; it is not in your best interests. You are often being shortchanged, and I intend to let you know why. Reviews This book makes you reflect on your health further and helps you “invest in prevention". It makes you bolder and more conscious of how to navigate the healthcare system. All in all, The Seasoned Steward is an eye-opener. Miriam Oswick, Certified Nutritionist Practitioner It pays to be informed and proactive with our health. If your goal is to become a smarter healthcare consumer and be more actively involved in your personal wellness, then The Seasoned Steward is required reading. Offering practical tips, principles and guidelines, this book is an important, straightforward resource to navigating the path of self-advocacy. Lorena Pavitt, Wellness Coach Once again, Dr. Imogen uses her experience, knowledge and research to give us the tools to take charge of our health. This is a gift. Imogen is an incredible researcher and brings forward a very balanced approach in her writings. Dr. Wendy Pruitt DDS. MBA The seasoned steward is “expertly” written. Dr. Haverly poses some thought-provoking questions that encourage one to change how they approach their health and retain some of the ‘power’ they have in influencing their own health and outcomes. Eleni Roula Papadimas BSc. Clinical Biologist, Consultant of Oncology unit, Kyrtos Hospital, Athens, Greece. Very interesting read! The book is written for You. It is very personable and relatable. Tons of useful and innovative information. Dr. Nino Gvelesiani, DDS About the author Dr. Imogen Haverly is an accomplished naturopathic doctor, author, blogger and speaker. She previously authored Canada’s most comprehensive book on food labels to date, The Savvy Pantry Keeper: A Primer on Grocery Tags and Tales. Her personal healing journey and triumph with fibromyalgia inspired her to become a relentless advocate for taking health into our own hands. This book is a continuation of that passion. Dr. Imogen, as @TheLectureMedic, dedicates much of her time teaching others how to think about their health.

Target Market(s)

Healthcare consumers. Ordinary people.

Industry/Entity Type

Health And Wellness

Font styles to use
Sans Serif
Other font styles liked:
• Simple and elegant

Colors
89d0c7
34a6d7

Requirements
Must have
• This book will be published
1) E-book in JPEG, PNG, TIFF
2) Printed book cover: 5.25"x8" (13.335x20.32 cm) (38,792 words)... pages about 160??? - provide in word file as well so I can edit
Image must be 2400X1600 pixels
3) Display of 3D book for advertisements
Nice to have
• *copy the design layout for my last book (BACK COVER) - attached
*attaching an example of an image from istock that is an EXAMPLE of a creative way to showing a patient being a SPECTATOR. I made a cover using it: https://www.pictovault-example.com/fr/vectoriel/calme-du-corps-gm908172635-71029384
*Nice elegant font (like in my example attached)
Should not have
• *avoid clipart of doctors or doctors with patients... this is too general

```html
<!DOCTYPE html>
<html lang="en">
<head>
<meta charset="utf-8">
<title>The Seasoned Steward — Front Cover</title>
<link rel="stylesheet" href="https://fonts.googleapis.com/css2?family=Oswald:wght@700&family=Roboto+Condensed:wght@700&display=swap">
<style>
  :root {
    --cover-blue: #3a8ee6;
    --cover-blue-deep: #2a74cc;
    --spot-light: #8cc4f5;
    --title-white: #ffffff;
    --title-shadow: #16283d;
    --author-navy: #0f2340;
    --hand-skin: #f6c9a0;
    --lens-rim: #3b3f48;
  }
  html, body {
    margin: 0;
    padding: 0;
    overflow: hidden;
    background: var(--cover-blue);
  }
  .cover {
    position: relative;
    width: 801px;
    height: 1200px;
    overflow: hidden;
    background: var(--cover-blue);
  }
  .cover-title {
    position: absolute;
    left: 0;
    top: 0;
    width: 801px;
    height: 340px;
  }
  .cover-title text {
    font-family: "Oswald", "Arial Narrow", sans-serif;
    font-weight: 700;
  }
  .title-face { fill: var(--title-white); }
  .title-shade { fill: var(--title-shadow); }
  .spotlight {
    position: absolute;
    left: 250px;
    top: 330px;
    width: 300px;
    height: 560px;
    background: linear-gradient(to bottom, rgba(140,196,245,0.55), rgba(140,196,245,0.05));
    clip-path: polygon(38% 0, 62% 0, 100% 100%, 0 100%);
  }
  .team-illustration {
    position: absolute;
    left: 228px;
    top: 420px;
    width: 445px;
    height: 440px;
    border-radius: 40px 40px 12px 12px;
    background: linear-gradient(to bottom, #e9eef3 0%, #c9d7e6 55%, #2c3e55 100%);
    opacity: 0.9;
  }
  .stage-floor {
    position: absolute;
    left: 210px;
    top: 845px;
    width: 480px;
    height: 36px;
    border-radius: 50%;
    background: var(--cover-blue-deep);
  }
  .magnifier-hand {
    position: absolute;
    left: 0;
    top: 530px;
    width: 200px;
    height: 670px;
    background: linear-gradient(to bottom, #a9d2f5 0%, #7fb5e8 28%, var(--lens-rim) 40%, var(--hand-skin) 60%, #eef2f6 100%);
    border-radius: 0 100px 0 0;
  }
  .subtitle {
    position: absolute;
    left: 200px;
    top: 892px;
    width: 470px;
    margin: 0;
    text-align: center;
    color: var(--title-white);
    font-family: "Roboto Condensed", "Arial Narrow", sans-serif;
    font-weight: 700;
    font-size: 42px;
    line-height: 56px;
  }
  .author {
    position: absolute;
    left: 200px;
    top: 1074px;
    width: 490px;
    margin: 0;
    text-align: center;
    color: var(--author-navy);
    font-family: "Roboto Condensed", "Arial Narrow", sans-serif;
    font-weight: 700;
    font-size: 20px;
    line-height: 30px;
  }
</style>
</head>
<body>
  <main class="cover">
    <svg class="cover-title" viewBox="0 0 801 340" aria-label="The Seasoned Steward">
      <text class="title-shade" x="44" y="176" textLength="730" lengthAdjust="spacingAndGlyphs" font-size="178">THE SEASONED</text>
      <text class="title-face" x="36" y="168" textLength="730" lengthAdjust="spacingAndGlyphs" font-size="178">THE SEASONED</text>
      <text class="title-shade" x="148" y="326" textLength="520" lengthAdjust="spacingAndGlyphs" font-size="178">STEWARD</text>
      <text class="title-face" x="140" y="318" textLength="520" lengthAdjust="spacingAndGlyphs" font-size="178">STEWARD</text>
    </svg>

    <div class="spotlight"></div>
    <div class="stage-floor"></div>
    <div class="team-illustration" role="img" aria-label="Illustration of four smiling doctors in white coats standing together under a spotlight"></div>
    <div class="magnifier-hand" role="img" aria-label="Illustration of a hand holding up a magnifying glass"></div>

    <p class="subtitle">Good Living isn't<br>a Bystander Game</p>
    <p class="author">Dr. Imogen Haverly, ND, MA (Inactive)<br>Doctor of Naturopathic Medicine</p>
  </main>
</body>
</html>
```